Kelvo Tech Oz Business card revamp

We are looking to revamp our business card design. We are hoping to change our colours to dark navey blue, gray, white and black but are open to keeping the same if a good design is submited. We are after somthing a bit differnt not just boring business card. I have attached a copy of our current card. We Want to keep the same logo design which i have attached a few to hopfully help you in this process. We are after a design that can be personalized to separate 4 people

Colors
0455a3
ffffff
000000
cbcbcb

Requirements
Must have
• Kelvo Tech Logo, address 3/41 Mallory Court, Wexhill 4218, phone number, Name and position

```html
<!DOCTYPE html>
<html lang="en">
<head>
<meta charset="utf-8">
<title>Kelvo Tech Oz – Business Card</title>
<link href="https://fonts.googleapis.com/css2?family=Open+Sans:wght@400;600&family=Ubuntu:wght@500;700&display=swap" rel="stylesheet">
<style>
  :root {
    --backdrop: #e4e4e4;
    --navy: #0a4a94;
    --blue: #0b57a8;
    --orange: #f37321;
    --slate: #4e5b7e;
    --white: #ffffff;
    --soft-blue: #2f7fd0;
  }
  * { box-sizing: border-box; margin: 0; padding: 0; }
  html, body { width: 1200px; height: 1200px; overflow: hidden; background: var(--backdrop); }
  .canvas { position: relative; width: 1200px; height: 1200px; }

  .card {
    position: absolute;
    width: 700px;
    height: 400px;
    overflow: hidden;
    box-shadow: 0 6px 18px rgba(0,0,0,0.18);
  }
  .card-accent { position: absolute; top: 0; right: 0; width: 100%; height: 100%; }

  /* Back side */
  .card-back { left: 80px; top: 130px; background: var(--navy); }
  .card-back .brand-block {
    position: absolute; left: 0; right: 0; top: 175px; text-align: center;
  }
  .brand-name {
    font-family: "Ubuntu", sans-serif;
    font-weight: 700;
    letter-spacing: 0.5px;
    display: inline-flex; align-items: center; gap: 12px;
  }
  .card-back .brand-name { color: var(--soft-blue); font-size: 54px; }
  .brand-dot { display: inline-block; border-radius: 50%; }
  .card-back .brand-dot { width: 30px; height: 30px; background: var(--orange); }
  .card-back .web {
    margin-top: 14px;
    font-family: "Open Sans", sans-serif;
    font-size: 26px; letter-spacing: 2px;
    color: var(--soft-blue);
  }

  /* Front side */
  .card-front { left: 420px; top: 660px; background: var(--blue); }
  .card-front .brand-name {
    position: absolute; left: 48px; top: 52px;
    color: var(--white); font-size: 44px;
  }
  .card-front .brand-dot { width: 26px; height: 26px; background: var(--white); }
  .person { position: absolute; left: 48px; top: 160px; font-family: "Ubuntu", sans-serif; }
  .person-name { color: var(--orange); font-size: 38px; font-weight: 500; letter-spacing: 1px; }
  .person-role { font-family: "Open Sans", sans-serif; color: var(--white); font-size: 19px; margin-top: 2px; }

  .contact-list { position: absolute; left: 48px; top: 268px; list-style: none; font-family: "Open Sans", sans-serif; color: var(--white); font-size: 18px; }
  .contact-list li { display: flex; align-items: center; gap: 12px; height: 30px; }
  .contact-list .divider { height: 1px; width: 560px; background: rgba(255,255,255,0.6); margin: 6px 0; }
  .icon { width: 20px; height: 20px; background: var(--orange); border-radius: 3px; display: inline-flex; align-items: center; justify-content: center; flex: none; }
  .icon svg { width: 14px; height: 14px; }
</style>
</head>
<body>
<main class="canvas">

  <section class="card card-back" aria-label="Business card back">
    <svg class="card-accent" viewBox="0 0 700 400" role="img" aria-label="Brand flame decoration area">
      <circle cx="640" cy="60" r="190" fill="var(--orange)"/>
    </svg>
    <div class="brand-block">
      <div class="brand-name"><span class="brand-dot"></span>Kelvo Tech</div>
      <div class="web">www.kelvotech.com.au</div>
    </div>
  </section>

  <section class="card card-front" aria-label="Business card front">
    <svg class="card-accent" viewBox="0 0 700 400" role="img" aria-label="Brand flame decoration area">
      <circle cx="640" cy="60" r="190" fill="var(--slate)"/>
    </svg>
    <div class="brand-name"><span class="brand-dot"></span>Kelvo Tech</div>
    <div class="person">
      <div class="person-name">JOHN DOE</div>
      <div class="person-role">Director</div>
    </div>
    <ul class="contact-list">
      <li>
        <span class="icon"><svg viewBox="0 0 16 16"><path d="M2 5c2-3 10-3 12 0l-2 2-2-1V5H6v1L4 7z M4 9h8l1 4H3z" fill="#fff"/></svg></span>
        1-234-567890
      </li>
      <li>
        <span class="icon"><svg viewBox="0 0 16 16" fill="none" stroke="#fff" stroke-width="1.3"><circle cx="8" cy="8" r="6"/><ellipse cx="8" cy="8" rx="2.6" ry="6"/><path d="M2 8h12"/></svg></span>
        www.companyname.com
      </li>
      <li class="divider"></li>
      <li>
        <span class="icon"><svg viewBox="0 0 16 16"><path d="M8 2l6 6h-2v6H4V8H2z" fill="#fff"/></svg></span>
        3/41 Mallory Court, Wexhill 4218
      </li>
    </ul>
  </section>

</main>
</body>
</html>
```